Attractive Flyer for Moving Company

Our Company called "Bluecrest Moving Company".
We provide moving service for home and businesses
We need a flyer for a moving company, located in San Diego, CA USA
Flyer size will be 7 x 5 inches, double sided.

Flyer needs to be very attractive and catchy for eye. I want people to keep it even if they dont need our service. I attached a lot of text in separate word file.
Logo, brief and additional pictures are attached.

Target Market(s)

27 years - 55 Years old

Industry/Entity Type

Moving Company

Colors
ec1f27
3176b5
ffffff

Requirements
Must have
• Attached in Word File
Nice to have
• Please be creative in placing a text and selecting a back ground picture.

```html
<!DOCTYPE html>
<html lang="en">
<head>
<meta charset="utf-8">
<title>Bluecrest Moving Company – Flyer</title>
<link href="https://fonts.googleapis.com/css2?family=Nunito:ital,wght@0,400;0,600;0,700;0,800;0,900;1,700&display=swap" rel="stylesheet">
<style>
:root{
  --red:#ec1f27;
  --red-dark:#b3121a;
  --blue:#3176b5;
  --blue-deep:#123a8a;
  --navy:#0d2a6b;
  --white:#ffffff;
  --ink:#222;
  --page:#2b2f33;
  --box-bg:#f1f2f4;
}
*{margin:0;padding:0;box-sizing:border-box}
html,body{width:867px;height:1200px;overflow:hidden;background:var(--page);font-family:"Nunito",sans-serif;color:var(--ink)}
.card{position:absolute;left:48px;width:765px;height:547px;background:var(--white);overflow:hidden}
.front{top:37px}
.back{top:613px}
.abs{position:absolute}

/* front header */
.header{left:0;top:0;width:765px;height:117px;background:var(--white);border-bottom:4px solid var(--red-dark)}
.brand{left:28px;top:30px;display:flex;align-items:center;gap:10px}
.brand-dot{width:14px;height:14px;border-radius:50%;background:var(--red)}
.brand-name{font-weight:900;font-size:24px;line-height:1.05;color:var(--red-dark)}
.tagline{left:304px;top:30px;font-style:italic;font-weight:700;font-size:18px;line-height:1.15;color:var(--red)}
.tagline span{color:var(--blue-deep)}
.license{left:305px;top:75px;font-size:10px;line-height:1.4;color:#333}
.badge-listing{left:609px;top:17px;width:52px;height:83px;border-radius:4px;background:var(--blue-deep);border:2px solid #d8e0f0}
.badge-review{left:667px;top:18px;width:80px;height:80px;border-radius:50%;background:var(--red)}

/* hero */
.hero-photo{left:0;top:121px;width:470px;height:150px;background:linear-gradient(180deg,#c9a47b 0%,#d9c2a4 55%,#fff 100%)}
.hero-fade{left:0;top:121px;width:765px;height:320px;background:linear-gradient(90deg,rgba(255,255,255,0) 0%,rgba(255,255,255,0) 58%,#f3f1ee 62%,#fff 100%)}
.boxes-photo{left:490px;top:348px;width:273px;height:150px;border-radius:8px 8px 0 0;background:linear-gradient(160deg,#d8b98c,#b98d5c)}
.why{left:472px;top:121px;width:280px;height:216px}
.why-content{left:490px;top:131px;width:258px;color:var(--white)}
.why-title{font-size:19px;font-weight:800;line-height:1.3;position:relative}
.stars{position:absolute;right:4px;top:3px;background:var(--white);color:var(--blue);border-radius:6px;font-size:10px;line-height:1.5;padding:0 6px;letter-spacing:1px}
.why-list{list-style:none;margin-top:6px;font-size:12px;line-height:1.2}
.why-list li{padding-left:16px;position:relative;margin-bottom:1px}
.why-list li::before{content:"✔";position:absolute;left:0;top:0;font-size:10px}
.headline{left:39px;top:252px;font-size:47px;line-height:1;font-weight:900;color:var(--red-dark);letter-spacing:-.5px}
.deals-line{left:38px;top:296px;font-size:16px;line-height:1.3;color:#333}
.deals-line small{font-size:10.5px}
.later-line{left:38px;top:319px;font-size:16px;line-height:1.3;color:#333}
.later-line strong{color:var(--blue-deep);font-weight:800}
.services{left:38px;top:356px;font-size:13px}
.services h3{font-size:14px;color:var(--red-dark);font-weight:800;margin-bottom:2px}
.services ul{list-style:none;display:flex;flex-wrap:wrap;width:320px;column-gap:20px;row-gap:1px}
.services li::before{content:"•";color:var(--blue);margin-right:8px}
.wave{left:0;width:765px}
.shout{left:38px;top:470px;color:var(--white);font-weight:800;font-size:23px;line-height:1.33}
.front-url{left:458px;top:509px;color:var(--white);font-weight:800;font-size:15px}

/* back */
.save{left:26px;top:18px;font-weight:900;font-size:51px;line-height:.86;color:var(--blue-deep);letter-spacing:-.5px}
.save span{color:var(--red-dark)}
.special{left:26px;top:114px;font-weight:900;font-size:35px;color:var(--red-dark)}
.note-small{left:26px;top:155px;font-size:16px;color:#333}
.promo{left:26px;top:180px;display:flex;align-items:center;gap:12px;font-size:22px;font-weight:900;color:var(--blue-deep)}
.promo-code{background:var(--red-dark);color:var(--white);padding:0 7px;font-size:22px}
.price{width:213px;height:84px;border:2px dashed var(--blue);border-radius:6px;background:var(--box-bg);text-align:center;padding-top:6px}
.price b{display:block;font-size:33px;font-weight:900;color:var(--red-dark);line-height:1.1}
.price p{font-size:11px;line-height:1.2;color:#333}
.price.off{padding-top:12px}
.price.off p{font-size:12.5px}
.extras{left:26px;top:410px;font-size:17px;line-height:1.22;color:var(--blue)}
.voucher{left:105px;top:455px;font-size:10px;color:#222}
.couple-photo{left:516px;top:28px;width:221px;height:152px;background:linear-gradient(135deg,#e8e2d8 0%,#b9cbe0 50%,#e7a6c2 100%)}
.included{left:516px;top:197px;width:235px}
.included h3{font-size:22px;font-weight:900;color:var(--red-dark);margin-bottom:8px}
.included ul{list-style:none;font-size:13.5px;line-height:1.22;color:#333}
.included li{padding-left:20px;position:relative}
.included li::before{content:"•";position:absolute;left:2px;color:var(--blue-deep);font-size:16px;line-height:1}
.terms{left:516px;top:341px;width:233px;height:123px;background:var(--blue-deep);color:var(--white);font-size:14px;line-height:1.22;text-align:center;padding:10px 8px}
.seal{left:372px;top:433px;width:96px;height:96px}
.back-url{left:26px;top:502px;color:var(--white);font-weight:900;font-size:19px;line-height:1}
.back-url small{display:block;font-size:13px;font-weight:600;margin-top:1px}
.call{right:24px;top:486px;text-align:right;color:var(--white);font-size:17px;line-height:1.25}
.call strong{display:block;font-size:20px;font-weight:900}
</style>
</head>
<body>

<section class="card front">
  <div class="abs hero-photo" role="img" aria-label="Photo of a smiling young couple sitting among moving boxes"></div>
  <div class="abs hero-fade"></div>

  <header class="abs header">
    <div class="abs brand"><span class="brand-dot"></span><div class="brand-name">Bluecrest<br>Moving Company</div></div>
    <div class="abs tagline">Quality Focused, <span>Customer<br>Recommended Movers</span></div>
    <div class="abs license">Licensed &amp; Fully Insured,<br>CAL PUC: #204837 US DOT: #30562914</div>
    <div class="abs badge-listing" role="img" aria-label="Accreditation badge"></div>
    <div class="abs badge-review" role="img" aria-label="Review site badge"></div>
  </header>

  <div class="abs boxes-photo" role="img" aria-label="Photo of stacked cardboard moving boxes with packing tape and tools"></div>

  <svg class="abs why" viewBox="0 0 280 216" aria-hidden="true">
    <defs><linearGradient id="whyGrad" x1="0" y1="0" x2="0" y2="1"><stop offset="0" stop-color="#0d2a6b"/><stop offset="1" stop-color="#1f4fae"/></linearGradient></defs>
    <polygon points="0,0 280,0 280,188 140,216 0,188" fill="url(#whyGrad)"/>
  </svg>
  <div class="abs why-content">
    <div class="why-title">Why Call Us? <span class="stars">★★★★★</span></div>
    <ul class="why-list">
      <li>Customer Oriented Service</li>
      <li>Years of Great reputation<br>(Lots of 5 Star Reviews)</li>
      <li>Affordable pricing</li>
      <li>Professional, efficient, strong movers</li>
      <li>We always handle your belongings<br>with care</li>
      <li>Clean and equipped trucks</li>
      <li>Absolutely NO surprising fees</li>
    </ul>
  </div>

  <h1 class="abs headline">Need MOVERS?</h1>
  <p class="abs deals-line">Take advantage of our SPECIAL DEALS <small>(see reverse side).</small></p>
  <p class="abs later-line"><strong>Not moving soon?</strong> Keep this flyer for later.</p>
  <div class="abs services">
    <h3>Moving Services:</h3>
    <ul><li>Residential</li><li>Long Distance</li><li>Commercial</li><li>Loading / Unloading</li><li>Packing Service</li></ul>
  </div>

  <svg class="abs wave" style="top:410px;height:137px" viewBox="0 0 765 137" preserveAspectRatio="none" aria-hidden="true">
    <defs><linearGradient id="redGradA" x1="0" y1="0" x2="1" y2="0"><stop offset="0" stop-color="#c8151d"/><stop offset=".5" stop-color="#ec1f27"/><stop offset="1" stop-color="#a8101a"/></linearGradient></defs>
    <path d="M0,38 Q200,-8 520,22 Q660,36 765,80 L765,137 L0,137Z" fill="#123a8a"/>
    <path d="M0,48 Q200,4 520,32 Q660,46 765,88 L765,137 L0,137Z" fill="url(#redGradA)"/>
  </svg>
  <p class="abs shout">Know someone who is moving?<br>Let them know about our deals!</p>
  <p class="abs front-url">www.BluecrestMoving.com</p>
</section>

<section class="card back">
  <h2 class="abs save">SAVE <span>10% -25%</span><br>ON YOUR MOVE</h2>
  <h3 class="abs special">Special Deals</h3>
  <p class="abs note-small">(Cannot be used with any other promotions or coupons)</p>
  <div class="abs promo">PROMOTION CODE: <span class="promo-code">BMC1016</span></div>

  <div class="abs price" style="left:25px;top:218px"><b>$255</b><p>3 hours of Moving Service with<br>2 PRO MOVERS &amp; TRUCK</p></div>
  <div class="abs price" style="left:249px;top:218px"><b>$345</b><p>3 hours of Moving Service with<br>3 PRO MOVERS &amp; TRUCK</p></div>
  <div class="abs price" style="left:25px;top:310px"><b>$435</b><p>3 hours of Moving Service with<br>4 PRO MOVERS &amp; TRUCK</p></div>
  <div class="abs price off" style="left:249px;top:310px"><b>$75 OFF</b><p>any Long Distance Move</p></div>

  <p class="abs extras">+ 20% OFF for boxes and packing supplies.<br>+ 3% OFF for cash payment</p>
  <p class="abs voucher">Keep this voucher it is valid until January 1, 2020</p>

  <div class="abs couple-photo" role="img" aria-label="Photo of a happy senior couple sitting back to back with coffee mugs among moving boxes"></div>
  <div class="abs included">
    <h3>INCLUDED IN PRICE</h3>
    <ul>
      <li>Protection of your furniture withspecialized blankets and plastic stretch wrap.</li>
      <li>Disassembly and reassembly of your furniture.</li>
      <li>Use of Wardrobe boxes</li>
    </ul>
  </div>
  <div class="abs terms">*Promotion code must be provided to our representative when requesting a quote and booking service appointment. *Promotion is valid for the first time customers ONLY</div>

  <svg class="abs wave" style="top:440px;height:107px" viewBox="0 0 765 107" preserveAspectRatio="none" aria-hidden="true">
    <defs><linearGradient id="redGradB" x1="0" y1="0" x2="1" y2="0"><stop offset="0" stop-color="#c8151d"/><stop offset=".5" stop-color="#ec1f27"/><stop offset="1" stop-color="#a8101a"/></linearGradient></defs>
    <path d="M0,12 Q260,52 480,44 Q640,36 765,8 L765,107 L0,107Z" fill="#123a8a"/>
    <path d="M0,22 Q260,62 480,54 Q640,46 765,18 L765,107 L0,107Z" fill="url(#redGradB)"/>
  </svg>
  <svg class="abs seal" viewBox="0 0 96 96" role="img" aria-label="Satisfaction guarantee seal">
    <circle cx="48" cy="48" r="46" fill="#e0b12a"/>
    <circle cx="48" cy="48" r="36" fill="#f4d35e"/>
  </svg>
  <p class="abs back-url">www.BluecrestMoving.com<small>Request your estimate online</small></p>
  <p class="abs call">Call For A Quick Estimate<strong>Toll Free: 1-855-555-0142</strong></p>
</section>

</body>
</html>
```